PowerPoint Design Project

Have a Power Point we want someone to make really cool! About 10 pages and just need someone to build on what we've done.

Target Market(s)

Technology Mfgs/VARs Sales People and VP of Sales

Industry/Entity Type

Build

```html
<!DOCTYPE html>
<html lang="en">
<head>
<meta charset="utf-8">
<title>Which ROI would your client prefer?</title>
<link href="https://fonts.googleapis.com/css2?family=PT+Sans+Narrow:wght@700&family=Arimo:wght@400;700&display=swap" rel="stylesheet">
<style>
  :root {
    --title-blue: #2f5f8f;
    --heading-blue: #1f4e79;
    --heading-green: #6b8e3a;
    --rule-grey: #a6a6a6;
    --frame-grey: #bfbfbf;
    --plot-lilac: #e6e0ec;
    --plot-green: #d7e4bd;
    --tag-green: #00a651;
    --bar-red: #c0392b;
    --bar-blue: #2e75c8;
    --line-red: #ff0000;
    --callout-grey: #d9d9d9;
    --callout-orange: #e46c0a;
    --brand-ink: #2f5f8f;
    --ink: #000;
  }
  html, body { margin: 0; padding: 0; overflow: hidden; }
  body { width: 1200px; height: 900px; background: #fff; font-family: "Arimo", Arial, sans-serif; }
  .slide { position: relative; width: 1200px; height: 900px; overflow: hidden; background: #fff; }
  .side-swoosh { position: absolute; left: 0; top: 0; }
  .slide-title {
    position: absolute; left: 244px; top: 28px; margin: 0;
    font-family: "PT Sans Narrow", "Arial Narrow", sans-serif; font-weight: 700;
    font-size: 60px; color: var(--title-blue); letter-spacing: 0.2px; white-space: nowrap;
  }
  .title-rule { position: absolute; left: 190px; top: 110px; width: 960px; height: 9px; background: var(--rule-grey); }
  .chart-heading { position: absolute; margin: 0; font-size: 23px; font-weight: 700; }
  .chart-heading.cash { left: 244px; top: 152px; color: var(--heading-blue); }
  .chart-heading.finance { left: 244px; top: 517px; color: var(--heading-green); }
  .chart { position: absolute; }
  .chart.cash { left: 234px; top: 194px; }
  .chart.finance { left: 233px; top: 559px; }
  .chart text { font-family: "Arimo", Arial, sans-serif; font-weight: 700; }
  .callout {
    position: absolute; left: 860px; top: 434px; width: 312px; height: 164px;
    background: var(--callout-grey); border-radius: 22px; box-sizing: border-box;
    padding: 14px 0 0 22px; color: var(--callout-orange); font-weight: 700; font-size: 30px; line-height: 41px;
  }
  .callout p { margin: 0; }
  .callout .first { padding-left: 3px; }
  .brand {
    position: absolute; right: 40px; top: 852px;
    color: var(--brand-ink); font-weight: 700; font-size: 18px; line-height: 22px; white-space: nowrap;
  }
</style>
</head>
<body>
<div class="slide">
  <svg class="side-swoosh" width="240" height="900" viewBox="0 0 240 900" role="img" aria-label="Decorative blue swoosh band along the left edge">
    <defs>
      <linearGradient id="swooshFill" x1="0" y1="0" x2="1" y2="0.3">
        <stop offset="0" stop-color="#0b2f6b"/>
        <stop offset="0.55" stop-color="#1a64b4"/>
        <stop offset="1" stop-color="#6fb6ea"/>
      </linearGradient>
    </defs>
    <path d="M0,0 L205,0 C160,220 130,520 148,900 L0,900 Z" fill="url(#swooshFill)"/>
    <path d="M205,0 C160,220 130,520 148,900" fill="none" stroke="#cfe6f7" stroke-width="3" opacity="0.7"/>
  </svg>

  <h1 class="slide-title">Which ROI would your client prefer?</h1>
  <div class="title-rule"></div>

  <h2 class="chart-heading cash">Cash or Net terms ROI</h2>
  <svg class="chart cash" width="675" height="279" viewBox="187 155 540 223">
    <rect x="187.5" y="155.5" width="539" height="222" fill="#fff" stroke="var(--frame-grey)"/>
    <rect x="213" y="195" width="412" height="155" fill="var(--plot-lilac)"/>
    <rect x="366" y="168" width="118" height="26" fill="var(--tag-green)"/>
    <text x="425" y="187" font-size="16" fill="#fff" text-anchor="middle">Cash Option</text>
    <line x1="213" y1="247" x2="625" y2="247" stroke="#999" stroke-width="1"/>
    <text x="207" y="252" font-size="11" text-anchor="end" fill="var(--ink)">$0</text>
    <g fill="var(--bar-red)">
      <rect x="251" y="247" width="10" height="40"/>
      <rect x="283" y="247" width="10" height="40"/>
    </g>
    <g fill="var(--bar-blue)">
      <rect x="324" y="240" width="9" height="7"/>
      <rect x="355" y="235" width="9" height="12"/>
      <rect x="387" y="235" width="9" height="12"/>
      <rect x="419" y="235" width="9" height="12"/>
      <rect x="451" y="235" width="9" height="12"/>
      <rect x="483" y="235" width="9" height="12"/>
      <rect x="514" y="235" width="9" height="12"/>
      <rect x="546" y="235" width="9" height="12"/>
      <rect x="578" y="235" width="9" height="12"/>
      <rect x="610" y="235" width="9" height="12"/>
    </g>
    <path d="M255,285 C266,302 280,330 302,323 L330,312 L608,202" fill="none" stroke="var(--line-red)" stroke-width="3"/>
    <g font-size="11" fill="var(--ink)" text-anchor="middle">
      <text x="260" y="370">Q1</text><text x="292" y="370">Q2</text><text x="324" y="370">Q3</text>
      <text x="355" y="370">Q4</text><text x="387" y="370">Q5</text><text x="419" y="370">Q6</text>
      <text x="451" y="370">Q7</text><text x="483" y="370">Q8</text><text x="514" y="370">Q9</text>
      <text x="546" y="370">Q10</text><text x="578" y="370">Q11</text><text x="610" y="370">Q12</text>
    </g>
    <rect x="633" y="240" width="8" height="7" fill="var(--bar-red)"/>
    <text x="644" y="247" font-size="11" fill="var(--ink)">Cash</text>
    <rect x="633" y="269" width="8" height="7" fill="var(--bar-blue)"/>
    <text x="644" y="276" font-size="11" fill="var(--ink)">Benefits</text>
    <line x1="630" y1="302" x2="642" y2="302" stroke="var(--line-red)" stroke-width="3"/>
    <text x="644" y="306" font-size="11" fill="var(--ink)">Net Cashflow</text>
  </svg>

  <h2 class="chart-heading finance">Financing or Leasing ROI</h2>
  <svg class="chart finance" width="679" height="275" viewBox="186 447 543 220">
    <rect x="186.5" y="447.5" width="542" height="219" fill="#fff" stroke="var(--frame-grey)"/>
    <rect x="216" y="486" width="412" height="152" fill="var(--plot-green)"/>
    <rect x="362" y="457" width="162" height="25" fill="var(--tag-green)"/>
    <text x="443" y="475" font-size="16" fill="#fff" text-anchor="middle">Payment Option</text>
    <line x1="216" y1="541" x2="628" y2="541" stroke="#999" stroke-width="1"/>
    <text x="214" y="550" font-size="12" text-anchor="end" fill="var(--ink)">$0</text>
    <g stroke="#999" stroke-width="1.5">
      <path d="M226,536 L236,546 M236,536 L226,546"/>
      <path d="M285,617 L295,627 M295,617 L285,627"/>
    </g>
    <g fill="var(--bar-red)">
      <rect x="341" y="541" width="8" height="9"/><rect x="370" y="541" width="8" height="9"/>
      <rect x="400" y="541" width="8" height="9"/><rect x="429" y="541" width="8" height="9"/>
      <rect x="458" y="541" width="8" height="9"/><rect x="487" y="541" width="8" height="9"/>
      <rect x="516" y="541" width="8" height="9"/><rect x="546" y="541" width="8" height="9"/>
      <rect x="575" y="541" width="8" height="9"/><rect x="604" y="541" width="8" height="7"/>
    </g>
    <g fill="var(--bar-blue)">
      <rect x="349" y="534" width="8" height="7"/><rect x="378" y="529" width="8" height="12"/>
      <rect x="408" y="529" width="8" height="12"/><rect x="437" y="529" width="8" height="12"/>
      <rect x="466" y="529" width="8" height="12"/><rect x="495" y="529" width="8" height="12"/>
      <rect x="524" y="529" width="8" height="12"/><rect x="554" y="529" width="8" height="12"/>
      <rect x="583" y="529" width="8" height="12"/><rect x="612" y="529" width="8" height="12"/>
    </g>
    <path d="M289,541 C318,543 338,547 360,541 L580,512 C596,509 606,505 615,500" fill="none" stroke="var(--line-red)" stroke-width="3"/>
    <g font-size="12" fill="var(--ink)" text-anchor="middle">
      <text x="290" y="661">Q1</text><text x="320" y="661">Q2</text><text x="350" y="661">Q3</text>
      <text x="379" y="661">Q4</text><text x="409" y="661">Q5</text><text x="438" y="661">Q6</text>
      <text x="467" y="661">Q7</text><text x="496" y="661">Q8</text><text x="523" y="661">Q9</text>
      <text x="551" y="661">Q10</text><text x="581" y="661">Q11</text><text x="611" y="661">Q12</text>
    </g>
    <rect x="636" y="499" width="8" height="7" fill="var(--bar-red)"/>
    <text x="648" y="507" font-size="12" fill="var(--ink)">Payments</text>
    <rect x="636" y="533" width="8" height="7" fill="var(--bar-blue)"/>
    <text x="648" y="541" font-size="12" fill="var(--ink)">Benefits</text>
    <line x1="633" y1="570" x2="646" y2="570" stroke="var(--line-red)" stroke-width="3"/>
    <text x="648" y="574" font-size="12" fill="var(--ink)">Net</text>
    <text x="648" y="591" font-size="12" fill="var(--ink)">Cashflow</text>
  </svg>

  <div class="callout">
    <p class="first">Same project</p>
    <p>Same benefits</p>
    <p>Quicker payback!</p>
  </div>

  <div class="brand">Harbor Lane Capital</div>
</div>
</body>
</html>
```